Real Estate Business card design

Company Name: Thornbury Holdings, LLC
subtitle: We pay cash for houses!
Martin Calloway
Managing Director
518-674-2913
Mart@ThornburyHoldingsLLC.example
www.ThornburyHoldingsLLC.example

We pay referral fees for Seller and Buyer leads.

Back:
We offer referral fees for Seller and Buyer leads that close.

Please contact Ned at 518-674-2913 with your referrals or to learn more about the referral program!

I am open to different color options but I am going for a classic, elegant, clean, and professional look. Please use logo as a reference.

Target Market(s)

People selling their homes and people in the market for buying homes.

Contact Information for Business Card

please see project description

Font styles to use
Serif
Sans Serif
Script

Requirements
Must have
• must have my logo in it
Nice to have
• I like cards that are split down the middle but please come up with a few mock ups. Open to any color scheme.

```html
<!DOCTYPE html>
<html lang="en">
<head>
<meta charset="utf-8">
<title>Thornbury Holdings, LLC – Business Card</title>
<link href="https://fonts.googleapis.com/css2?family=Source+Sans+3:ital,wght@0,400;0,600;0,700;1,400&display=swap" rel="stylesheet">
<style>
  :root {
    --page: #e8e5e0;
    --paper: #f7f7f5;
    --slate: #3f4856;
    --slate-deep: #394250;
    --tan: #c9a27a;
    --ink: #545a63;
    --white: #ffffff;
  }
  * { box-sizing: border-box; margin: 0; padding: 0; }
  html, body {
    width: 1125px; height: 1200px; overflow: hidden;
    background: var(--page);
    font-family: "Source Sans 3", "Myriad Pro", sans-serif;
  }
  .canvas { position: relative; width: 1125px; height: 1200px; }

  .card {
    position: absolute; left: 150px; width: 825px; height: 471px;
    border-radius: 26px; overflow: hidden;
    box-shadow: 0 4px 10px rgba(0,0,0,.25);
  }
  .card--front { top: 100px; background: var(--paper); }
  .card--back  { top: 633px; background: var(--slate); }

  /* front */
  .name-band { position: absolute; left: 0; top: 127px; width: 640px; height: 88px; }
  .holder { position: absolute; left: 78px; top: 137px; color: var(--white); }
  .holder__name { font-weight: 700; font-size: 31px; line-height: 1.1; letter-spacing: .2px; }
  .holder__title { font-size: 19px; color: var(--tan); margin-top: 2px; }

  .contacts { position: absolute; left: 78px; top: 267px; list-style: none; }
  .contacts li {
    display: flex; align-items: center; gap: 9px;
    font-size: 18px; color: var(--ink); line-height: 25px;
  }
  .contacts svg { width: 15px; height: 15px; flex: none; fill: var(--tan); }

  .brand { position: absolute; left: 455px; top: 205px; width: 330px; text-align: center; }
  .brand__mark {
    display: block; width: 22px; height: 22px; margin: 0 auto 10px;
    background: var(--tan);
  }
  .brand__name {
    font-weight: 600; font-size: 33px; line-height: 1.05; color: var(--slate);
  }
  .brand__tagline {
    font-weight: 700; font-size: 22px; color: var(--ink); margin-top: 8px;
  }

  /* back */
  .back-brand { position: absolute; left: 0; right: 0; top: 120px; text-align: center; }
  .back-brand__mark { display: block; width: 46px; height: 46px; margin: 0 auto 22px; background: var(--tan); }
  .back-brand__name { font-weight: 600; font-size: 52px; color: var(--tan); letter-spacing: .5px; }

  .referral {
    position: absolute; left: 0; right: 0; top: 350px;
    text-align: center; color: var(--white); font-size: 18px; line-height: 24px;
  }
  .referral em { font-style: italic; }
  .referral strong { font-weight: 700; }
</style>
</head>
<body>
<main class="canvas">

  <section class="card card--front" aria-label="Card front">
    <svg class="name-band" viewBox="0 0 640 88" aria-hidden="true">
      <polygon points="0,0 588,0 500,88 0,88" fill="var(--slate)"/>
    </svg>
    <div class="holder">
      <p class="holder__name">Martin Calloway</p>
      <p class="holder__title">President</p>
    </div>

    <ul class="contacts">
      <li>
        <svg viewBox="0 0 16 16" aria-hidden="true"><path d="M3.6 1.2l2.3 2.6-1.2 2a9 9 0 0 0 5.5 5.5l2-1.2 2.6 2.3-1.3 2.4C7.2 16.5-.5 8.8 1.2 2.5z"/></svg>
        <span>518-674-2913</span>
      </li>
      <li>
        <svg viewBox="0 0 16 16" aria-hidden="true"><path d="M1 3h14v10H1z M1.5 3.5 8 9l6.5-5.5" stroke="var(--paper)" stroke-width="1.2"/></svg>
        <span>Mart@ThornburyHoldingsLLC.example</span>
      </li>
      <li>
        <svg viewBox="0 0 16 16" aria-hidden="true"><circle cx="8" cy="8" r="7"/><path d="M4 5c2 0 2 2 4 2s1 3-1 3-1 3-3 2M10 2c0 2 2 2 3 3" stroke="var(--paper)" stroke-width="1.1" fill="none"/></svg>
        <span>ThornburyHoldingsLLC.example</span>
      </li>
    </ul>

    <div class="brand">
      <span class="brand__mark" aria-hidden="true"></span>
      <p class="brand__name">Thornbury Holdings, LLC</p>
      <p class="brand__tagline">We Pay Cash For Houses</p>
    </div>
  </section>

  <section class="card card--back" aria-label="Card back">
    <div class="back-brand">
      <span class="back-brand__mark" aria-hidden="true"></span>
      <p class="back-brand__name">Thornbury Holdings, LLC</p>
    </div>
    <div class="referral">
      <p>We offer <strong>Referral Fees for Seller &amp; Buyer</strong> leads That Close.</p>
      <p><em>Please</em> <strong>Contact Ned at 518-674-2913 with your referrals</strong> <em>or</em></p>
      <p><em>to learn more about the Referral program!</em></p>
    </div>
  </section>

</main>
</body>
</html>
```